Brisk Haven Web Site design

I need to build an exciting, colorful web site to market our business. I already used your services to design our logo with Torvend. Design # 12613143.
Our company sells a trademarked system for cleaning up water damage in buildings across the United States. This work is billed directly through insurance companies and has a high profit margin.

Target Market(s)

Men. 25-55 yrs old who want to own there own business

Industry/Entity Type

Cleaning Service

Number of Pages Required

4 page

Font styles to use
Sans Serif

Requirements
Must have
• Our trademarked logo as designed by Torvend
• Our phone number: 833-4BRISKY (833-442-7759)
• Pictures of flooded homes and businesses.
• List of our services: Water removal, carpet and tile cleaning, mold remediation, and trauma clean up services.
• Photos of our truck as designed by Torvend
• Photos of an attractive operator standing buy to take a call.
• Photos of happy homeowners
Nice to have
• Call to action text
• "Proven system"text
• "Be your own boss" text

```html
<!DOCTYPE html>
<html lang="en">
<head>
<meta charset="utf-8">
<title>Brisk Haven</title>
<link rel="stylesheet" href="https://fonts.googleapis.com/css2?family=Roboto:wght@400;500;700&family=Open+Sans:wght@300;400;600&family=Lato:wght@400;700&display=swap">
<style>
:root{
  --blue:#1a63ae;
  --blue-dark:#0d4f94;
  --red:#c4161c;
  --ink:#333;
  --muted:#7a7a7a;
  --grey-circle:#e9e9e9;
  --white:#fff;
  --footer-text:#555;
}
*{margin:0;padding:0;box-sizing:border-box}
html,body{width:1200px;height:2332px;overflow:hidden;background:var(--white)}
body{position:relative;font-family:"Open Sans",Arial,sans-serif;color:var(--ink)}
.abs{position:absolute}

/* header */
.site-header{left:0;top:0;width:1200px;height:82px;background:var(--white)}
.brand{left:126px;top:24px;font-family:"Roboto",sans-serif;font-weight:500;font-size:28px;color:var(--blue);letter-spacing:-.5px}
.hotline{right:128px;top:14px;text-align:right;font-family:"Roboto",sans-serif}
.hotline-number{display:flex;align-items:center;gap:10px;font-size:29px;font-weight:700;color:var(--blue)}
.hotline-number .red{color:var(--red)}
.hotline-note{font-size:12px;color:#666;letter-spacing:.5px;margin-top:-2px}

/* nav */
.main-nav{left:0;top:82px;width:1200px;height:50px;background:var(--blue)}
.main-nav ul{list-style:none;position:absolute;left:126px;top:0;display:flex;height:50px}
.main-nav li{font-family:"Roboto",sans-serif;font-size:13.5px;font-weight:500;color:var(--white);line-height:50px;padding:0 12px}
.main-nav li.active{background:var(--red);width:90px;text-align:center;padding:0;margin-right:12px}
.nav-social{right:128px;top:0;display:flex;height:50px}
.nav-social span{width:36px;height:50px;border-left:1px solid rgba(255,255,255,.25);display:flex;align-items:center;justify-content:center}
.nav-social span:last-child{border-right:1px solid rgba(255,255,255,.25)}
.nav-social i{width:10px;height:10px;border-radius:50%;background:rgba(255,255,255,.7)}

/* hero */
.hero-photo{left:0;top:132px;width:1200px;height:539px;background:linear-gradient(180deg,#b9c7cf 0%,#8fa6b3 45%,#4e6f84 75%,#2b4a60 100%)}
.hero-panel{left:549px;top:289px;width:508px;height:247px;background:rgba(0,0,0,.72);padding:22px 34px}
.hero-kicker{font-family:"Roboto",sans-serif;font-size:43px;font-weight:500;color:#1f74c9;line-height:1}
.hero-title{font-family:"Roboto",sans-serif;font-size:39px;font-weight:400;color:var(--white);line-height:1.05}
.hero-copy{font-family:"Roboto",sans-serif;font-size:12.5px;font-weight:700;color:var(--white);line-height:1.3;margin-top:10px;width:370px}
.hero-actions{display:flex;gap:10px;margin-top:16px}
.btn{font-family:"Roboto",sans-serif;font-size:14px;font-weight:500;color:var(--white);height:43px;line-height:43px;padding:0 13px}
.btn-blue{background:var(--blue)}
.btn-red{background:var(--red);padding:0 20px}

/* sections */
.section-title{width:1200px;left:0;text-align:center;font-family:"Lato",sans-serif;font-weight:700;font-size:29px;color:var(--blue)}
.section-lede{left:220px;width:760px;text-align:center;font-weight:300;font-size:17px;line-height:25px;color:#666}
.service{width:260px;text-align:center}
.service-icon{width:146px;height:146px;border-radius:50%;background:var(--grey-circle);margin:0 auto;display:flex;align-items:center;justify-content:center}
.service-icon.featured{background:var(--blue)}
.service-name{font-family:"Roboto",sans-serif;font-size:17px;margin-top:14px;color:#222}
.section-divider{left:0;top:1070px;width:1200px;height:14px;background:linear-gradient(180deg,#f1f1f1,#fff)}

.reason-photo{left:117px;top:1246px;width:943px;height:380px;background:linear-gradient(90deg,#3b5d8c 0%,#c9c9c6 30%,#e5e2dc 65%,#8d7d72 100%)}
.reason-card{left:207px;top:1346px;width:788px;height:328px;background:var(--white);box-shadow:0 6px 20px rgba(0,0,0,.18)}
.reason-copy{left:31px;top:47px;width:330px}
.reason-copy h3{font-family:"Lato",sans-serif;font-weight:400;font-size:21px;line-height:26px;color:var(--blue)}
.reason-copy p{font-family:"Lato",sans-serif;font-size:13.5px;line-height:25px;color:#666;margin-top:20px}
.reason-link{display:inline-block;margin-top:34px;font-family:"Lato",sans-serif;font-size:14px;color:var(--red);text-decoration:underline}
.reason-rule{left:388px;top:66px;width:1px;height:190px;background:#ddd}
.testimonial{left:457px;top:66px;width:275px}
.testimonial .quote-mark{position:absolute;left:-10px;top:-14px;font-family:Georgia,serif;font-size:70px;color:#e4e4e4;line-height:1}
.testimonial p{position:relative;font-family:"Lato",sans-serif;font-size:13px;line-height:24.5px;color:#666}
.testimonial cite{display:block;margin-top:18px;font-style:normal;font-family:"Lato",sans-serif;font-size:13px;font-weight:700;color:#222}
.testimonial cite em{font-weight:400;font-size:10px;font-style:italic}

/* contact band */
.contact-map{left:0;top:1737px;width:572px;height:352px;background:linear-gradient(135deg,#eceef0,#dfe3e6)}
.contact-info{left:131px;top:1775px}
.band-title{font-family:"Roboto",sans-serif;font-weight:700;font-size:30px;letter-spacing:-.5px}
.contact-info .band-title{color:var(--blue)}
.contact-info .hours-title{color:var(--red);margin-top:22px}
.contact-line{font-family:"Lato",sans-serif;font-size:15.5px;color:#333;margin-top:6px}
.contact-row{font-family:"Lato",sans-serif;font-size:13.5px;color:#333;margin-top:4px}
.contact-row b{font-weight:400;color:var(--blue);display:inline-block;width:54px}
.hours{font-family:"Lato",sans-serif;font-size:12px;color:#222;margin-top:6px;line-height:18px}
.hours span{display:inline-block;width:95px}
.newsletter{left:572px;top:1737px;width:628px;height:352px;background:var(--blue-dark)}
.newsletter-notch{left:-20px;top:130px}
.newsletter .band-title{position:absolute;left:49px;top:57px;color:var(--white);font-weight:500;font-size:32px}
.field{position:absolute;left:49px;width:436px;height:54px;background:var(--white);border-radius:3px;font-family:"Lato",sans-serif;font-size:13px;color:#888;line-height:54px;padding-left:15px}
.subscribe{position:absolute;left:49px;top:250px;width:436px;height:37px;background:var(--red);border-radius:3px;text-align:center;line-height:37px;font-family:"Roboto",sans-serif;font-weight:500;font-size:17px;color:var(--white);letter-spacing:.5px}

/* footer */
.footer-col h4{font-family:"Roboto",sans-serif;font-weight:500;font-size:29px;color:var(--blue);letter-spacing:-.3px}
.footer-about p{font-family:"Lato",sans-serif;font-size:12.5px;line-height:23px;color:var(--footer-text);margin-top:12px;width:300px}
.footer-links ul{list-style:none;display:grid;grid-template-columns:188px 150px;margin-top:14px;row-gap:5px}
.footer-links li{font-family:"Lato",sans-serif;font-size:12.5px;color:var(--footer-text)}
.social-dots{display:flex;gap:13px;margin-top:15px}
.social-dots span{width:40px;height:40px;border-radius:50%;background:var(--blue-dark)}
.social-dots span:nth-child(2){background:#2a8fd3}
.social-dots span:nth-child(4){background:#dd4b39}
.footer-rule{left:0;top:2326px;width:1200px;height:6px;background:var(--blue)}
</style>
</head>
<body>

<header class="site-header abs">
  <div class="brand abs">BRISK HAVEN</div>
  <div class="hotline abs">
    <div class="hotline-number">
      <svg width="26" height="26" viewBox="0 0 26 26"><circle cx="13" cy="13" r="13" fill="#c4161c"/><path d="M9 7l3 3-2 2c1 2 2 3 4 4l2-2 3 3-2 2c-5 0-10-5-10-10z" fill="#fff"/></svg>
      <span class="red">833-4BRISKY</span><span>(833-442-7759)</span>
    </div>
    <div class="hotline-note">24/7 EMERGENCY SERVICE</div>
  </div>
</header>

<nav class="main-nav abs">
  <ul>
    <li class="active">Home</li>
    <li>Services</li>
    <li>Commercial Services</li>
    <li>Emergency Services</li>
    <li>About us</li>
    <li>Request Appointment</li>
  </ul>
  <div class="nav-social abs"><span><i></i></span><span><i></i></span><span><i></i></span><span><i></i></span></div>
</nav>

<div class="hero-photo abs" role="img" aria-label="Smiling technician in work overalls holding a clipboard inside a flooded kitchen"></div>
<div class="hero-panel abs">
  <div class="hero-kicker">PROVEN SYSTEM</div>
  <div class="hero-title">BE YOUR OWN BOSS</div>
  <p class="hero-copy">Lorem ipsum dolor sit amet, consectetuer adipiscing elit, sed diam nonummy nibh euismod tincidunt ut laoreet dolore magna aliquam erat volutpat.</p>
  <div class="hero-actions">
    <span class="btn btn-blue">REQUEST AN APPOINTMENT</span>
    <span class="btn btn-red">WATCH VIDEO</span>
  </div>
</div>

<h2 class="section-title abs" style="top:708px">Brisk Haven Services</h2>
<p class="section-lede abs" style="top:760px">Lorem ipsum dolor sit amet, consectetuer adipiscing elit, sed diam nonummy nibh euismod tincidunt ut laoreet dolore magna aliquam erat volutpat.</p>

<div class="service abs" style="left:92px;top:841px">
  <div class="service-icon featured">
    <svg width="56" height="72" viewBox="0 0 56 72"><path d="M28 2C20 20 6 34 6 48a22 22 0 0044 0C50 34 36 20 28 2z" fill="#fff"/><path d="M18 46c0 8 4 13 10 15" stroke="#1a63ae" stroke-width="5" fill="none" stroke-linecap="round"/></svg>
  </div>
  <div class="service-name">Water removal</div>
</div>
<div class="service abs" style="left:318px;top:841px">
  <div class="service-icon">
    <svg width="80" height="96" viewBox="0 0 80 96"><circle cx="48" cy="10" r="9" fill="#1a63ae"/><path d="M38 24h20l4 36h-8l-2 34h-8l-3-30-8 4-10 18h-6l12-26 7-10z" fill="#1a63ae"/><path d="M40 34L22 80" stroke="#1a63ae" stroke-width="4"/><rect x="8" y="78" width="22" height="10" rx="3" fill="#1a63ae"/></svg>
  </div>
  <div class="service-name">Carpet and tile cleaning</div>
</div>
<div class="service abs" style="left:566px;top:841px">
  <div class="service-icon">
    <svg width="84" height="70" viewBox="0 0 84 70"><ellipse cx="42" cy="35" rx="30" ry="20" fill="#1a63ae" transform="rotate(-25 42 35)"/><g stroke="#1a63ae" stroke-width="4" stroke-linecap="round"><path d="M16 52l-8 6M24 60l-4 8M40 60l0 8M58 50l8 6M68 36l10 0M70 22l8-6M58 12l4-9M42 12l-2-9M24 22l-8-6M14 38l-10 2"/></g><g fill="#fff"><circle cx="32" cy="34" r="3"/><circle cx="46" cy="28" r="3"/><circle cx="52" cy="40" r="3"/><circle cx="38" cy="44" r="2"/></g></svg>
  </div>
  <div class="service-name">Mold remediation</div>
</div>
<div class="service abs" style="left:820px;top:841px">
  <div class="service-icon">
    <svg width="84" height="96" viewBox="0 0 84 96"><path d="M66 4v58" stroke="#1a63ae" stroke-width="4"/><path d="M56 60h20l6 30H50z" fill="#1a63ae"/><path d="M10 60l26-10 10 24-26 10z" fill="#1a63ae"/><path d="M36 50l10-8" stroke="#1a63ae" stroke-width="4"/></svg>
  </div>
  <div class="service-name">Trauma clean up services</div>
</div>

<div class="section-divider abs"></div>

<h2 class="section-title abs" style="top:1126px">Great Reasons to Choose Brisk Haven</h2>
<p class="section-lede abs" style="top:1168px">Lorem ipsum dolor sit amet, consectetuer adipiscing elit, sed diam nonummy nibh euismod tincidunt ut laoreet dolore magna aliquam erat volutpat.</p>

<div class="reason-photo abs" role="img" aria-label="Plumber in a cap working under a kitchen sink while a homeowner looks on"></div>
<article class="reason-card abs">
  <div class="reason-copy abs">
    <h3>Saving Water<br>Means Saving Money</h3>
    <p>Lorem ipsum dolor sit amet, consectetuer adipiscing elit, sed diam nonummy nibh euismod tincidunt ut laoreet dolore magna aliquam erat volutpat.</p>
    <span class="reason-link">View Case Studies</span>
  </div>
  <div class="reason-rule abs"></div>
  <blockquote class="testimonial abs">
    <span class="quote-mark">&ldquo;</span>
    <p>Dalton is an outstanding Linden tax attorney. He is responsive, thorough, and creative in his advice, and he is also genuinely collegial with others. He is a valued advisor to Corvane and other Meridex divisions.</p>
    <cite>Harlan Ostby &ndash; <em>Manager Director</em></cite>
  </blockquote>
</article>

<section>
  <div class="contact-map abs" role="img" aria-label="Faded street map around the office location with a map pin"></div>
  <div class="contact-info abs">
    <div class="band-title">CONTACT US</div>
    <div class="contact-line">Marlow Springs, AL 35090</div>
    <div class="contact-row" style="margin-top:14px"><b>Phone:</b>833-4BRISKY &nbsp; - &nbsp; (833-442-7759)</div>
    <div class="contact-row"><b>Email:</b>info@briskhaven.com</div>
    <div class="band-title hours-title">REGULAR BUSINESS HOURS</div>
    <div class="hours">
      <div><span>Monday-Friday</span>7:00am-7:00pm</div>
      <div><span>Saturday</span>9:00am-4:00pm</div>
      <div><span>Sunday</span>9:00am-2:00pm</div>
    </div>
  </div>
  <div class="newsletter abs">
    <svg class="newsletter-notch abs" width="20" height="44" viewBox="0 0 20 44"><path d="M20 0v44L0 22z" fill="#0d4f94"/></svg>
    <div class="band-title">NEWSLETTER SIGN-UP</div>
    <div class="field" style="top:122px">Your Name</div>
    <div class="field" style="top:185px">Your Email</div>
    <div class="subscribe">SUBSCRIBE</div>
  </div>
</section>

<footer>
  <div class="footer-col footer-about abs" style="left:127px;top:2126px">
    <h4>ABOUT BRISK HAVEN</h4>
    <p>Lorem ipsum dolor sit amet, consectetuer adipiscing elit, sed diam nonummy nibh euismod tincidunt ut laoreet dolore magna aliquam erat volutpat.</p>
  </div>
  <div class="footer-col footer-links abs" style="left:465px;top:2126px">
    <h4>QUICK LINKS</h4>
    <ul>
      <li>Residential Services</li><li>Commercial Services</li>
      <li>Franchise Opportunities</li><li>Site Map</li>
      <li>About Us</li><li>Contact Us</li>
      <li>Privacy Policy</li><li>Terms &amp; Conditions</li>
      <li>Careers</li>
    </ul>
  </div>
  <div class="footer-col abs" style="left:817px;top:2126px">
    <h4>CONNECT WITH US</h4>
    <div class="social-dots"><span></span><span></span><span></span><span></span></div>
  </div>
  <div class="footer-rule abs"></div>
</footer>

</body>
</html>
```